Harwell Lawyers Banner

I would like to have a graphic design created for a company banner. The company is Harwell Lawyers and the website is https://harwelllawyers-example.com.au/ We would like a professional banner we are able to put up at events to advertise the company.
The banner size is 800mm wide by 2000mm high so please keep the design inside these constraints.

```html
<!DOCTYPE html>
<html lang="en">
<head>
<meta charset="utf-8">
<title>Harwell Lawyers – Event Banner Options</title>
<link href="https://fonts.googleapis.com/css2?family=Montserrat:ital,wght@0,300;0,400;0,800;1,300;1,400;1,800;1,900&display=swap" rel="stylesheet">
<style>
  :root{
    --page:#e8e8e8;
    --navy:#273a5b;
    --blue:#1e9ad6;
    --tan:#c9a07c;
    --copper:#b4733e;
    --copper-dark:#8a5428;
    --pill:#d4a47f;
    --white:#ffffff;
  }
  *{box-sizing:border-box;margin:0;padding:0}
  html,body{width:1200px;height:1200px;overflow:hidden;background:var(--page)}
  body{position:relative;font-family:"Montserrat",Arial,sans-serif}

  .banner{position:absolute;top:214px;width:309px;height:772px;overflow:hidden;background:var(--navy);color:var(--white)}
  .banner--one{left:30px}
  .banner--two{left:445px}
  .banner--three{left:861px}

  .banner__photo{position:absolute;left:0;top:0;width:100%;height:480px}
  .banner--one .banner__photo{background:linear-gradient(180deg,#b9bec3 0%,#7d8794 22%,#46546c 55%,rgba(39,58,91,0) 100%)}
  .banner--two .banner__photo{background:linear-gradient(160deg,#7fb2da 0%,#8b8068 25%,#5c5a55 45%,rgba(39,58,91,0) 100%)}
  .banner--three .banner__photo{background:linear-gradient(180deg,#1c2e4c 0%,#59677d 28%,#7f8796 45%,rgba(39,58,91,0) 100%)}

  .banner__ground{position:absolute;left:0;bottom:0;width:100%;height:26px;
    background:linear-gradient(90deg,var(--copper) 0%,var(--copper-dark) 100%)}

  .line{position:absolute;left:0;right:0;text-align:center;line-height:1;white-space:nowrap}

  .brand__name{top:26px;font-weight:300;font-size:48px;letter-spacing:3px}
  .brand__sub{top:89px;left:auto;right:18px;font-weight:300;font-size:16px;letter-spacing:5px;color:var(--blue);text-align:right}

  .tagline{left:37px;right:auto;text-align:left;font-style:italic}
  .tagline--lead{top:130px;font-weight:300;font-size:19.5px}
  .tagline--firm{top:148px;font-weight:900;font-size:41px;color:var(--blue)}
  .tagline--spec{top:188px;font-weight:300;font-size:26px}

  .service{font-style:italic;font-weight:900;letter-spacing:-0.2px}
  .detail{font-style:italic;font-weight:300;color:var(--tan);letter-spacing:0.3px}

  .advising{top:234px;font-size:32px}
  .advising-d{top:268px;font-size:15.7px}
  .estate{top:298px;font-size:27.5px}
  .estate-d{top:330px;font-size:15.5px}
  .tax{top:358px;left:16px;right:auto;font-size:37px}
  .tax-d{top:395px;left:17px;right:auto;font-size:6px}
  .planning{top:359px;left:auto;right:18px;font-size:29.5px}
  .planning-d{top:389px;left:auto;right:18px;font-size:16px}
  .nfp{top:419px;font-size:29.5px}
  .nfp-d{top:450px;font-size:19.5px}
  .mgmt{top:484px;font-size:23px}
  .mgmt-d{top:510px;font-size:16px}
  .lit{top:540px;font-size:33px}
  .lit-d{top:574px;font-size:14px}

  .divider{position:absolute;top:603px;height:1.5px;width:97px;background:var(--blue)}
  .divider--left{left:41px}
  .divider--right{left:172px}

  .clients__label{position:absolute;left:33px;top:677px;transform-origin:0 0;transform:rotate(-90deg);white-space:nowrap;line-height:1}
  .clients__our{font-style:italic;font-weight:900;font-size:21px}
  .clients__word{display:block;font-style:italic;font-weight:300;font-size:11px;color:var(--tan);letter-spacing:0.5px}
  .clients__list{position:absolute;left:71px;top:617px;list-style:none;font-style:italic;font-weight:300;font-size:10.5px;line-height:15px}

  .contact__pill{position:absolute;left:173px;top:689px;width:100px;height:19px;border-radius:10px;background:var(--pill);
    font-style:italic;font-weight:800;font-size:10.5px;line-height:19px;text-align:center;color:var(--white)}
  .contact__phone{top:711px;left:auto;right:16px;font-style:italic;font-weight:900;font-size:20px;color:var(--blue)}
  .contact__email{top:732px;left:auto;right:18px;font-weight:300;font-size:9.5px}
</style>
</head>
<body>

<section class="banner banner--one">
  <div class="banner__photo" role="img" aria-label="Photograph of a judge's gavel, fading into navy"></div>
  <div class="banner__ground" role="img" aria-label="Copper textured paper band"></div>
  <div class="line brand__name">HARWELL</div>
  <div class="line brand__sub">LAWYERS</div>
  <div class="line tagline tagline--lead">LEADING COMMERCIAL</div>
  <div class="line tagline tagline--firm">LAW FIRM</div>
  <div class="line tagline tagline--spec">SPECIALISING IN</div>
  <div class="line service advising">ADVISING</div>
  <div class="line detail advising-d">FAMILY BUSINESSES</div>
  <div class="line service estate">ESTATE PLANNING</div>
  <div class="line detail estate-d">ADMINISTRATION AND DISPUTES</div>
  <div class="line service tax">TAX</div>
  <div class="line detail tax-d">AND STRUCTURING</div>
  <div class="line service planning">PLANNING</div>
  <div class="line detail planning-d">AND ENVIRONMENT</div>
  <div class="line service nfp">NOT FOR PROFIT</div>
  <div class="line detail nfp-d">AND SOCIAL ENTERPRISE</div>
  <div class="line service mgmt">MANAGEMENT RIGHTS</div>
  <div class="line detail mgmt-d">PROPERTY AND DEVELOPMENTS</div>
  <div class="line service lit">LITIGATION</div>
  <div class="line detail lit-d">AND DISPUTE RESOLUTION</div>
  <div class="divider divider--left"></div>
  <div class="divider divider--right"></div>
  <div class="clients__label"><span class="clients__our">OUR</span><span class="clients__word">CLIENTS</span></div>
  <ul class="clients__list">
    <li>Private Clients and Family Businesses</li>
    <li>Startups and New Businesses</li>
    <li>Established Organisations</li>
    <li>Professional Advisors</li>
  </ul>
  <div class="contact__pill">CONTACT US</div>
  <div class="line contact__phone">07 5550 1234</div>
  <div class="line contact__email">info@harwelllawyers-example.com.au</div>
</section>

<section class="banner banner--two">
  <div class="banner__photo" role="img" aria-label="Photograph of a stone courthouse column against the sky, fading into navy"></div>
  <div class="banner__ground" role="img" aria-label="Copper textured paper band"></div>
  <div class="line brand__name">HARWELL</div>
  <div class="line brand__sub">LAWYERS</div>
  <div class="line tagline tagline--lead">LEADING COMMERCIAL</div>
  <div class="line tagline tagline--firm">LAW FIRM</div>
  <div class="line tagline tagline--spec">SPECIALISING IN</div>
  <div class="line service advising">ADVISING</div>
  <div class="line detail advising-d">FAMILY BUSINESSES</div>
  <div class="line service estate">ESTATE PLANNING</div>
  <div class="line detail estate-d">ADMINISTRATION AND DISPUTES</div>
  <div class="line service tax">TAX</div>
  <div class="line detail tax-d">AND STRUCTURING</div>
  <div class="line service planning">PLANNING</div>
  <div class="line detail planning-d">AND ENVIRONMENT</div>
  <div class="line service nfp">NOT FOR PROFIT</div>
  <div class="line detail nfp-d">AND SOCIAL ENTERPRISE</div>
  <div class="line service mgmt">MANAGEMENT RIGHTS</div>
  <div class="line detail mgmt-d">PROPERTY AND DEVELOPMENTS</div>
  <div class="line service lit">LITIGATION</div>
  <div class="line detail lit-d">AND DISPUTE RESOLUTION</div>
  <div class="divider divider--left"></div>
  <div class="divider divider--right"></div>
  <div class="clients__label"><span class="clients__our">OUR</span><span class="clients__word">CLIENTS</span></div>
  <ul class="clients__list">
    <li>Private Clients and Family Businesses</li>
    <li>Startups and New Businesses</li>
    <li>Established Organisations</li>
    <li>Professional Advisors</li>
  </ul>
  <div class="contact__pill">CONTACT US</div>
  <div class="line contact__phone">07 5550 1234</div>
  <div class="line contact__email">info@harwelllawyers-example.com.au</div>
</section>

<section class="banner banner--three">
  <div class="banner__photo" role="img" aria-label="Photograph of a business handshake, fading into navy"></div>
  <div class="banner__ground" role="img" aria-label="Copper textured paper band"></div>
  <div class="line brand__name">HARWELL</div>
  <div class="line brand__sub">LAWYERS</div>
  <div class="line tagline tagline--lead">LEADING COMMERCIAL</div>
  <div class="line tagline tagline--firm">LAW FIRM</div>
  <div class="line tagline tagline--spec">SPECIALISING IN</div>
  <div class="line service advising">ADVISING</div>
  <div class="line detail advising-d">FAMILY BUSINESSES</div>
  <div class="line service estate">ESTATE PLANNING</div>
  <div class="line detail estate-d">ADMINISTRATION AND DISPUTES</div>
  <div class="line service tax">TAX</div>
  <div class="line detail tax-d">AND STRUCTURING</div>
  <div class="line service planning">PLANNING</div>
  <div class="line detail planning-d">AND ENVIRONMENT</div>
  <div class="line service nfp">NOT FOR PROFIT</div>
  <div class="line detail nfp-d">AND SOCIAL ENTERPRISE</div>
  <div class="line service mgmt">MANAGEMENT RIGHTS</div>
  <div class="line detail mgmt-d">PROPERTY AND DEVELOPMENTS</div>
  <div class="line service lit">LITIGATION</div>
  <div class="line detail lit-d">AND DISPUTE RESOLUTION</div>
  <div class="divider divider--left"></div>
  <div class="divider divider--right"></div>
  <div class="clients__label"><span class="clients__our">OUR</span><span class="clients__word">CLIENTS</span></div>
  <ul class="clients__list">
    <li>Private Clients and Family Businesses</li>
    <li>Startups and New Businesses</li>
    <li>Established Organisations</li>
    <li>Professional Advisors</li>
  </ul>
  <div class="contact__pill">CONTACT US</div>
  <div class="line contact__phone">07 5550 1234</div>
  <div class="line contact__email">info@harwelllawyers-example.com.au</div>
</section>

</body>
</html>
```